現在販売している商品(シリーズ商品)のデザイン変更を計画しております。
今回は表ラベルのデザインをお願い致します。

この商品は個食タイプの商品で現在は表ラベルを共通にして、4種類の味(たまり醤油・七味唐辛子・ねぎみそ・柚子こしょう)を販売しております。今後も入れ替えをしながらいろいろな味を販売していく予定です。

販売チャネルとしては、スーパーや企業売店などの米菓コーナーや個食コーナーです。

商品形態は、バラ詰めしたせんべい2枚を、無地袋に表ラベル(共通で使用)と味ラベルを貼付ます。(添付写真を参照)

商品の特徴として、
1.国産うるち米100%使用
2.それぞれの味で使用している調味料(しょうゆ・だし・香辛料)にもこだわりがある
3.一枚一枚に厚みがあり食べ応えがある本格派せんべい

商品サイズ:縦180m/m × 横140m/m
ラベルサイズ:縦85(±10)× 横40(±10)サイズ内での変形も可能
色数:3色程度で
紙質:和紙(雲龍)タイプを考えております。

シリーズものとして、制作して頂くラベルの脇に味ラベル(既存ラベル)を貼り付けます。

デザインイメージとしては、
品名は縦書き
和紙の風合いを活かし、シンプルで高級感をだす
ワンポイントとなるコピーやイラストを入れる

※現在使用しているラベルのコピー「伝統の味」は使わないでください。

大変選考に時間が掛かり申し訳ございません。
どのデザインも素晴らしく迷いましたが、
選考のポイントは、
①文字の見やすさ
②シンプルで分かりやすい
③全体のバランス
です。

この度は多数のご提案を頂きありがとうございました。
商品に特徴(ポイント)が無く、難しい案件かなと思っていましたが
思った以上に素晴らしいデザインで迷いました。
これからの皆様にご依頼することがあると思いますので
今後ともよろしくお願いいたします。

```html
<!DOCTYPE html>
<html lang="ja">
<head>
<meta charset="UTF-8">
<title>せんべい 表ラベル</title>
<link rel="stylesheet" href="https://fonts.googleapis.com/css2?family=Shippori+Mincho+B1:wght@500;700;800&display=swap">
<style>
  :root {
    --bg: #f2f1ef;
    --rust: #b4542b;
    --rust-light: #c0653a;
    --rust-deep: #9e4522;
    --cream: #f8f3ea;
    --ink-brown: #6a2a16;
    --title-red: #a8361f;
    --seal-red: #b22a1f;
    --gold: #e2c07a;
    --gold-light: #f3e2b4;
  }
  * { margin: 0; padding: 0; box-sizing: border-box; }
  html, body {
    width: 850px; height: 1200px; overflow: hidden;
    background: var(--bg);
  }
  .label {
    position: absolute;
    left: 195px; top: 100px;
    width: 460px; height: 1000px;
    overflow: hidden;
    background: var(--rust);
    box-shadow: 0 2px 10px rgba(0,0,0,0.12);
    font-family: "Shippori Mincho B1", serif;
  }
  .label-pattern {
    position: absolute; inset: 0;
    background: linear-gradient(160deg, var(--rust-light) 0%, var(--rust) 55%, var(--rust-deep) 100%);
  }
  .medallion {
    position: absolute;
    left: 30px; top: 90px;
    width: 800px; height: 800px;
    margin-left: -190px;
    border-radius: 50%;
    background: radial-gradient(circle at 50% 50%, #ffffff 0%, var(--cream) 70%, #efe6d6 100%);
    box-shadow: 0 0 0 5px var(--gold);
  }
  .tagline {
    position: absolute;
    left: 362px; top: 150px;
    writing-mode: vertical-rl;
    font-size: 30px; font-weight: 700;
    letter-spacing: 0.08em;
    line-height: 1;
    color: var(--ink-brown);
  }
  .product-name {
    position: absolute;
    left: 140px; top: 255px;
    writing-mode: vertical-rl;
    font-size: 136px; font-weight: 800;
    line-height: 1;
    letter-spacing: 0;
    color: var(--title-red);
  }
  .seal {
    position: absolute;
    left: 336px; top: 640px;
    width: 40px; height: 78px;
    background: var(--seal-red);
    color: var(--cream);
    writing-mode: vertical-rl;
    font-size: 28px; font-weight: 700;
    line-height: 1;
    display: flex; align-items: center; justify-content: center;
    border-radius: 3px;
  }
  .rice-band {
    position: absolute;
    left: 0; right: 0; top: 905px;
    height: 72px;
    background: linear-gradient(90deg, var(--gold) 0%, var(--gold-light) 50%, var(--gold) 100%);
    display: flex; align-items: center; justify-content: center;
    color: var(--ink-brown);
    font-size: 32px; font-weight: 700;
    letter-spacing: 0.1em;
  }
</style>
</head>
<body>
  <div class="label">
    <div class="label-pattern" role="img" aria-label="麻の葉文様の地模様"></div>
    <div class="medallion"></div>
    <div class="tagline">本格厚焼き・こだわりの味</div>
    <h1 class="product-name">せんべい</h1>
    <div class="seal">謹製</div>
    <div class="rice-band">うるち米 100%</div>
  </div>
</body>
</html>
```